A property investment company, looking to provide lovely sustainable homes for familys and individua

For a small investment business i am starting which will buy and refurbish unloved houses and apartments to rent out or resell. the company name is my family surname (HARGREAVE). <br/>i would like the design to be simple with maybe some emphasis on an ethical and sustainable/environmentally friendly approach with a branding of maybe trees blended with some houses and or apartments.<br/>The colours i like for this design would be mainly green on either a white or black background.
Target Market(s)
This business card is to be used for professional people such as estate agents
mortgage brokers, solicitors and trades people.
Industry/Entity Type
Real Estate
Contact Information for Business Card
owner/director-Martin hargreave
e-mail-martin@hvholdings.co.uk
website-hargreavehomeholdings.co.uk
mobile-07700945318
landline-02079460581
Look and feel

```html
<!DOCTYPE html>
<html lang="en">
<head>
<meta charset="utf-8">
<title>Hargreave Business Card</title>
<link rel="stylesheet" href="https://fonts.googleapis.com/css2?family=Jost:wght@300;400;500&family=Arimo:wght@400&display=swap">
<style>
  :root {
    --brand-green: #41ae4a;
    --ink: #231f20;
    --paper: #ffffff;
    --edge: #1a1a1a;
  }
  * { margin: 0; padding: 0; box-sizing: border-box; }
  html, body { width: 1200px; height: 1200px; overflow: hidden; background: var(--paper); }
  body { position: relative; font-family: "Jost", sans-serif; }

  .card {
    position: absolute;
    left: 202px;
    width: 803px;
    height: 520px;
    overflow: hidden;
  }
  .card--front { top: 58px; background: var(--paper); border: 1px solid var(--edge); }
  .card--back { top: 634px; background: var(--brand-green); }

  .front-wave { position: absolute; inset: 0; width: 100%; height: 100%; }
  .front-wave path { fill: var(--brand-green); }

  .brand-lockup {
    position: absolute;
    top: 50px;
    left: 0; right: 0;
    text-align: center;
  }
  .brand-lockup__row {
    display: inline-flex;
    align-items: center;
    gap: 14px;
  }
  .brand-mark-dot {
    width: 78px; height: 78px;
    border-radius: 50%;
    background: var(--brand-green);
  }
  .brand-name {
    font-weight: 500;
    font-size: 50px;
    line-height: 1;
    letter-spacing: 1px;
    color: var(--brand-green);
  }
  .brand-tagline {
    margin-top: 8px;
    font-weight: 400;
    font-size: 25px;
    letter-spacing: 3.5px;
    color: var(--ink);
  }

  .contact-block {
    position: absolute;
    top: 248px;
    left: 0; right: 0;
    text-align: center;
    color: var(--paper);
  }
  .contact-block__name { font-weight: 500; font-size: 44px; line-height: 1.1; letter-spacing: 0.5px; }
  .contact-block__role { font-weight: 300; font-size: 27px; line-height: 1.2; }
  .contact-block__details {
    margin-top: 40px;
    font-weight: 300;
    font-size: 27px;
    line-height: 36px;
    letter-spacing: 0.3px;
  }

  .back-lockup {
    position: absolute;
    top: 118px;
    left: 0; right: 0;
    display: flex;
    justify-content: center;
    align-items: center;
    gap: 26px;
  }
  .back-lockup__dot {
    width: 180px; height: 180px;
    border-radius: 50%;
    background: var(--paper);
  }
  .back-lockup__name {
    font-weight: 500;
    font-size: 86px;
    line-height: 1;
    color: var(--paper);
  }
  .back-services {
    position: absolute;
    top: 380px;
    left: 0; right: 0;
    text-align: center;
    font-family: "Arimo", sans-serif;
    font-size: 37px;
    color: var(--paper);
    letter-spacing: 0.3px;
  }
</style>
</head>
<body>

<section class="card card--front">
  <svg class="front-wave" viewBox="0 0 803 520" preserveAspectRatio="none" aria-hidden="true">
    <path d="M0,262 C22,240 58,223 94,223 L646,223 C722,223 770,192 803,146 L803,520 L0,520 Z"/>
  </svg>

  <div class="brand-lockup">
    <div class="brand-lockup__row">
      <span class="brand-mark-dot"></span>
      <span class="brand-name">HARGREAVE</span>
    </div>
    <div class="brand-tagline">PROPERTY INVESTMENT</div>
  </div>

  <div class="contact-block">
    <div class="contact-block__name">Martin Hargreave</div>
    <div class="contact-block__role">Managing Director</div>
    <div class="contact-block__details">
      <div>Lorem Ipsum, Consectetur, Adipiscing AB1 2CD</div>
      <div>T: 02079460581&nbsp;&nbsp;E: martin@hvholdings.co.uk</div>
      <div>W: www.hargreavehomeholdings.co.uk</div>
    </div>
  </div>
</section>

<section class="card card--back">
  <div class="back-lockup">
    <span class="back-lockup__dot"></span>
    <span class="back-lockup__name">HARGREAVE</span>
  </div>
  <div class="back-services">BUY | REFURBISH | RENT | RESELL</div>
</section>

</body>
</html>
```